We need a business card design for a Dubai based company .

We need a business card for a Dubai based company called "Zernova Smoking Requisites Trading LLC". We mainly import Flavoured Tobacco products and Charcoal which is used for smoking in a Hookah/Shisha and distribute to the wholesalers and retailers. Logo file is attached herewith.

```html
<!DOCTYPE html>
<html lang="en">
<head>
<meta charset="utf-8">
<title>Zernova Smoking Requisites Trading LLC — Business Card</title>
<link href="https://fonts.googleapis.com/css2?family=Arimo:wght@400;700&family=Montserrat:wght@500&display=swap" rel="stylesheet">
<style>
  :root {
    --backdrop: #cdcdce;
    --card-light: #f4f4f3;
    --card-dark: #262626;
    --ink: #2a2a2a;
    --ink-soft: #3a3a3a;
    --accent: #b5232a;
    --rule: #6a6a6a;
    --on-dark: #f2f2f2;
  }
  * { margin: 0; padding: 0; box-sizing: border-box; }
  html, body { width: 1200px; height: 788px; overflow: hidden; }
  body {
    background: var(--backdrop);
    font-family: "Arimo", Arial, sans-serif;
    position: relative;
  }
  .card {
    position: absolute;
    top: 251px;
    width: 500px;
    height: 286px;
    box-shadow: 0 6px 16px rgba(0,0,0,0.18);
  }
  .card--front { left: 60px; background: var(--card-light); }
  .card--back { left: 640px; background: var(--card-dark); display: flex; align-items: center; justify-content: center; }

  .brand {
    display: flex;
    align-items: center;
    gap: 12px;
  }
  .brand__mark { width: 14px; height: 14px; background: var(--accent); flex: none; }
  .brand__name {
    font-family: "Montserrat", Arial, sans-serif;
    font-weight: 500;
    text-transform: uppercase;
    letter-spacing: 0.12em;
    line-height: 1.35;
  }
  .card--front .brand {
    position: absolute;
    left: 34px;
    top: 112px;
    width: 200px;
  }
  .card--front .brand__name { color: var(--ink); font-size: 13px; }
  .card--back .brand__name { color: var(--on-dark); font-size: 17px; }

  .divider {
    position: absolute;
    left: 248px;
    top: 66px;
    width: 1px;
    height: 154px;
    background: var(--rule);
  }
  .contact {
    position: absolute;
    left: 272px;
    top: 62px;
    color: var(--ink);
    font-size: 12px;
    line-height: 1.3;
  }
  .contact__name { color: var(--accent); font-weight: 700; font-size: 16px; }
  .contact__role { margin-bottom: 12px; font-size: 12.5px; }
  .contact__list { list-style: none; margin-bottom: 12px; }
  .contact__list li { display: flex; align-items: center; gap: 7px; }
  .contact__list svg { width: 10px; height: 10px; flex: none; }
  .contact__address { color: var(--ink-soft); font-style: normal; }
</style>
</head>
<body>
  <section class="card card--front" aria-label="Card front">
    <div class="brand">
      <span class="brand__mark"></span>
      <span class="brand__name">Zernova Smoking Requisites Trading LLC</span>
    </div>
    <div class="divider"></div>
    <div class="contact">
      <p class="contact__name">Rohan Mehta</p>
      <p class="contact__role">Sales Manager</p>
      <ul class="contact__list">
        <li>
          <svg viewBox="0 0 10 10" aria-hidden="true"><path d="M2 1 L4 1 L4.6 3 L3.4 3.8 Q4.4 5.8 6.2 6.6 L7 5.4 L9 6 L9 8 Q8.6 9 7.6 9 Q1 8 1 2.4 Q1 1.4 2 1 Z" fill="var(--accent)"/></svg>
          123.456.7890
        </li>
        <li>
          <svg viewBox="0 0 10 10" aria-hidden="true"><rect x="0.8" y="2" width="8.4" height="6" fill="none" stroke="var(--accent)" stroke-width="1.1"/><path d="M0.8 2 L5 5.4 L9.2 2" fill="none" stroke="var(--accent)" stroke-width="1.1"/></svg>
          mehta@zernova.com
        </li>
        <li>
          <svg viewBox="0 0 10 10" aria-hidden="true"><circle cx="5" cy="5" r="4.2" fill="none" stroke="var(--accent)" stroke-width="1"/><ellipse cx="5" cy="5" rx="1.8" ry="4.2" fill="none" stroke="var(--accent)" stroke-width="0.9"/><path d="M0.8 5 H9.2" stroke="var(--accent)" stroke-width="0.9"/></svg>
          www.zernova.com
        </li>
      </ul>
      <address class="contact__address">
        Unit KLM 0X<br>
        Jade Bazaar Dubai Int. City<br>
        Dubai AE
      </address>
    </div>
  </section>

  <section class="card card--back" aria-label="Card back">
    <div class="brand">
      <span class="brand__mark"></span>
      <span class="brand__name">Zernova</span>
    </div>
  </section>
</body>
</html>
```